BRAMBLE CABS

Taxi card design

Need changes very slow in replying to my messages.

Target Market(s)

Customers

Industry/Entity Type

Taxi

Contact Information for Business Card

See previous design

Font styles to use
Sans Serif

Colors
A7469A
B969AE
D3A5CF
EDDBEB
F8F0F9
6B429C
8869AF
B7A5CE
E3DAEB
F3F0F8

Requirements
Nice to have
• We are in the business of looking after people, not just driving vehicles front
Should not have
• Front number 01832 419 526 needs to big big

```html
<!DOCTYPE html>
<html lang="en">
<head>
<meta charset="utf-8">
<title>Bramble Cabs – Business Card</title>
<link href="https://fonts.googleapis.com/css2?family=Poppins:wght@400;500;600;700&display=swap" rel="stylesheet">
<style>
  :root{
    --plum:#9a3395;
    --plum-mid:#7f2e8e;
    --violet:#6b429c;
    --deep-violet:#5c2a84;
    --check:#b36aae;
    --check-dark:#4e2277;
    --ink:#141414;
    --text:#2a2a2a;
    --white:#ffffff;
    --backdrop:#ddd8d6;
  }
  *{box-sizing:border-box;margin:0;padding:0}
  html,body{width:670px;height:1200px;overflow:hidden}
  body{background:var(--backdrop);font-family:'Poppins',sans-serif;position:relative}

  .card{position:absolute;left:100px;width:469px;height:268px;overflow:hidden;
        box-shadow:0 6px 12px rgba(0,0,0,.22)}
  .card--front{top:290px;background:linear-gradient(90deg,var(--plum),var(--deep-violet))}
  .card--back{top:612px;background:var(--white)}

  /* front */
  .checker-strip{position:absolute;top:0;bottom:40px;width:33px;opacity:.35}
  .checker-strip--left{left:0;background:var(--check)}
  .checker-strip--right{right:0;background:var(--check-dark)}
  .front-name{position:absolute;top:88px;left:0;right:0;text-align:center;
              color:var(--white);font-weight:700;font-size:38px;letter-spacing:.5px;line-height:1}
  .front-wave{position:absolute;left:0;top:0}
  .front-call{position:absolute;left:212px;top:198px;width:37px;height:37px;border-radius:50%;
              border:3px solid var(--violet);background:var(--white);display:flex;align-items:center;justify-content:center}
  .front-number{position:absolute;left:0;right:0;top:237px;text-align:center;color:var(--ink);
                font-weight:600;font-size:17px;letter-spacing:4px}
  .front-edge{position:absolute;left:0;right:0;bottom:0;height:4px;
              background:linear-gradient(90deg,var(--violet),var(--plum))}

  /* back */
  .back-name{position:absolute;left:20px;top:18px;font-weight:700;font-size:21px;color:var(--ink);line-height:1}
  .back-badge{position:absolute;left:20px;top:54px;display:flex;align-items:center;gap:2px;font-weight:700;font-size:11px;color:var(--ink)}
  .back-badge__box{border:2px solid var(--violet);padding:0 3px;line-height:16px}
  .contact-list{position:absolute;left:20px;top:96px;list-style:none}
  .contact-item{display:flex;align-items:flex-start;gap:10px;font-size:11px;color:var(--text);line-height:17px;margin-bottom:4px}
  .contact-icon{flex:0 0 17px;width:17px;height:17px;border-radius:3px;background:var(--violet);
                display:flex;align-items:center;justify-content:center}

  .service-panel{position:absolute;left:270px;top:0;width:199px;height:268px;
                 background:linear-gradient(180deg,var(--plum),var(--plum-mid) 55%,var(--deep-violet))}
  .panel-checks{position:absolute;left:0;right:0;height:34px;opacity:.3;background:var(--check-dark)}
  .panel-checks--top{top:14px}
  .panel-checks--bottom{bottom:10px;border-bottom-left-radius:20px}
  .service-list{position:absolute;left:15px;top:76px;list-style:none}
  .service-item{display:flex;align-items:center;gap:12px;color:var(--white);font-weight:500;font-size:14.5px;line-height:23px}
  .hotline{position:absolute;left:270px;top:166px;width:199px;height:36px;background:var(--white);
           display:flex;align-items:center;gap:10px;padding-left:16px}
  .hotline__number{font-weight:600;font-size:20px;color:var(--ink);letter-spacing:.2px}
  .panel-corner{position:absolute;left:270px;top:202px;width:20px;height:66px;background:var(--white)}
  .panel-corner::after{content:"";position:absolute;inset:0;background:linear-gradient(180deg,var(--violet),var(--deep-violet));border-bottom-left-radius:20px}
</style>
</head>
<body>

<section class="card card--front" aria-label="Card front">
  <div class="checker-strip checker-strip--left" role="img" aria-label="Checkered taxi pattern strip"></div>
  <div class="checker-strip checker-strip--right" role="img" aria-label="Checkered taxi pattern strip"></div>
  <h1 class="front-name">Bramble Cabs</h1>
  <svg class="front-wave" width="469" height="268" viewBox="0 0 469 268" aria-hidden="true">
    <path d="M0 236 Q0 230 20 229 Q60 228 100 216 Q140 193 168 192 L282 192 Q310 194 330 215 Q345 231 362 231 L469 231 L469 268 L0 268 Z" fill="#fff"/>
  </svg>
  <div class="front-call">
    <svg width="18" height="18" viewBox="0 0 24 24" aria-hidden="true">
      <path d="M6.6 10.8a15 15 0 0 0 6.6 6.6l2.2-2.2c.3-.3.7-.4 1-.2 1.1.4 2.3.6 3.6.6.6 0 1 .4 1 1V20c0 .6-.4 1-1 1A17 17 0 0 1 3 4c0-.6.4-1 1-1h3.5c.6 0 1 .4 1 1 0 1.3.2 2.5.6 3.6.1.3 0 .7-.2 1z" fill="#141414"/>
      <path d="M14 3a7 7 0 0 1 7 7M14 6.5A3.5 3.5 0 0 1 17.5 10" stroke="#141414" stroke-width="1.8" fill="none" stroke-linecap="round"/>
    </svg>
  </div>
  <p class="front-number">01832 419 526</p>
  <div class="front-edge"></div>
</section>

<section class="card card--back" aria-label="Card back">
  <h2 class="back-name">Bramble Cabs</h2>
  <p class="back-badge"><span class="back-badge__box">24/7</span>Service</p>

  <ul class="contact-list">
    <li class="contact-item">
      <span class="contact-icon"><svg width="10" height="10" viewBox="0 0 24 24"><path d="M6.6 10.8a15 15 0 0 0 6.6 6.6l2.2-2.2c.3-.3.7-.4 1-.2 1.1.4 2.3.6 3.6.6.6 0 1 .4 1 1V20c0 .6-.4 1-1 1A17 17 0 0 1 3 4c0-.6.4-1 1-1h3.5c.6 0 1 .4 1 1 0 1.3.2 2.5.6 3.6.1.3 0 .7-.2 1z" fill="#fff"/></svg></span>
      <span>01832 41 77 10<br>01832 30 30 30<br>01832 41 62 08</span>
    </li>
    <li class="contact-item">
      <span class="contact-icon"><svg width="11" height="11" viewBox="0 0 24 24"><path d="M2 9c3-4 17-4 20 0l-3 2-3-2V7H8v2l-3 2zM6 12h12l2 8H4z" fill="#fff"/></svg></span>
      <span>0800 555 0 184</span>
    </li>
    <li class="contact-item">
      <span class="contact-icon"><svg width="11" height="11" viewBox="0 0 24 24"><rect x="3" y="6" width="18" height="13" rx="1" fill="#fff"/><path d="M3 7l9 6 9-6" stroke="#6b429c" stroke-width="2" fill="none"/></svg></span>
      <span>hello@bramblecabs.co.uk</span>
    </li>
    <li class="contact-item">
      <span class="contact-icon"><svg width="10" height="11" viewBox="0 0 24 24"><path d="M12 2a7 7 0 0 0-7 7c0 5 7 13 7 13s7-8 7-13a7 7 0 0 0-7-7zm0 9.5A2.5 2.5 0 1 1 12 6.5a2.5 2.5 0 0 1 0 5z" fill="#fff"/></svg></span>
      <span style="line-height:14px">Holly Lane Community Hall<br>Mill Road Oundle PE8 4QT</span>
    </li>
    <li class="contact-item">
      <span class="contact-icon"><svg width="11" height="11" viewBox="0 0 24 24"><circle cx="12" cy="12" r="9" stroke="#fff" stroke-width="2" fill="none"/><path d="M3 12h18M12 3c3 3 3 15 0 18M12 3c-3 3-3 15 0 18" stroke="#fff" stroke-width="1.6" fill="none"/></svg></span>
      <span>www.bramblecabs.co.uk</span>
    </li>
  </ul>

  <div class="service-panel">
    <div class="panel-checks panel-checks--top" role="img" aria-label="Checkered taxi pattern band"></div>
    <ul class="service-list">
      <li class="service-item"><svg width="13" height="11" viewBox="0 0 24 20"><path d="M9 1h6v3H9zM4 9l2-5h12l2 5h2v7h-3v3h-3v-3H8v3H5v-3H2V9z" fill="#fff"/></svg>Airport Transfers</li>
      <li class="service-item"><svg width="13" height="11" viewBox="0 0 24 20"><path d="M9 1h6v3H9zM4 9l2-5h12l2 5h2v7h-3v3h-3v-3H8v3H5v-3H2V9z" fill="#fff"/></svg>Minibuses</li>
      <li class="service-item"><svg width="13" height="11" viewBox="0 0 24 20"><path d="M9 1h6v3H9zM4 9l2-5h12l2 5h2v7h-3v3h-3v-3H8v3H5v-3H2V9z" fill="#fff"/></svg>School Transport</li>
    </ul>
    <div class="panel-checks panel-checks--bottom" role="img" aria-label="Checkered taxi pattern band"></div>
  </div>
  <div class="panel-corner"></div>
  <div class="hotline">
    <svg width="19" height="19" viewBox="0 0 24 24" aria-hidden="true">
      <path d="M6.6 10.8a15 15 0 0 0 6.6 6.6l2.2-2.2c.3-.3.7-.4 1-.2 1.1.4 2.3.6 3.6.6.6 0 1 .4 1 1V20c0 .6-.4 1-1 1A17 17 0 0 1 3 4c0-.6.4-1 1-1h3.5c.6 0 1 .4 1 1 0 1.3.2 2.5.6 3.6.1.3 0 .7-.2 1z" fill="none" stroke="#6b429c" stroke-width="1.8"/>
      <path d="M14 3a7 7 0 0 1 7 7M14 6.5A3.5 3.5 0 0 1 17.5 10" stroke="#6b429c" stroke-width="1.8" fill="none" stroke-linecap="round"/>
    </svg>
    <span class="hotline__number">01832 419 526</span>
  </div>
</section>

</body>
</html>
```